7 Herons Distillery - Bottle Label Design

We are a small craft distillery whose branding needs to incorporate our location on a lake (Lac Vernisse, Quebec, Canada). A unique aspect of the lake is that people drive floating docks on the lake powered by a small outboard motor (see photos). Back in the 1970’s when Lac Vernisse was a sparsely populated and difficult-to-access lake in the Gatineau Hills north of Ottawa, the concept of motorized docks was conjured on a lazy afternoon and this single stroke of genius has inadvertently spawned the most exceptional and eccentric lake based community. Throughout the summer, somewhere around four o’clock on any given Friday and Saturday it starts to happen. Docks set sail from their customary landing places - family, friends, snacks and loaded drink coolers in-tow and, as if magnetically drawn, head toward Pine Shoal. Without fail they will come upon a gathering of similar minded floating docks within the vicinity - be guided in with help to moor alongside and within seconds be seamlessly immersed in the festivities. Seldom any longer are these events planned, they have become elemental, a thing organically derived from within the community. This on-going weekly event is the genesis of the strong bond that brings us Seven Herons Distilling.
Each of the 4 distillery owners have one of these docks so hence the name. We are open to either "7 Herons" or spelled out as "Seven Herons" as may be visually appropriate. We are also open to "Distillery" or "Distilling". More detail on the docks themselves, they are 14x16 feet powered by a small outboard motor as shown in the photos. This dock aspect may be difficult to incorporate into the branding but the lake outline is included as an image applicable to include for that local reference aspect. We will be creating very high quality small batch liquors such as vodka, rum, gin and whiskey. Each batch will be triple distilled and perhaps 20 bottles in quantity so very exclusive. We are aiming at a premium feel for the branding. Attached are some bottle label designs that evoke the type of feel we are going for and a photo of the style of blank bottle to design for which is a 750ml Nordic pattern bottle.
In general we are going for more contemporary than traditional, more bold than delicate. If a single label the size desired would be 4 inches wide and 4 inches tall. If a double/split label as in two of the photos the top label would be 3 inches wide and 3 inches tall and the bottom label would be max 4 inches wide and 1.5 inches tall. We are open to the upper label being a "transparent" label to create a printed on bottle effect, perhaps of the brand logo. We are only interested in front label so do not require a back, neck or closure label. The label will require the ability to name the batch style name (example "Tuberix") and then the amplifying information for the type of alcohol (Russian Potato Vodka) in a smaller font. Another example ("Red Fox" and "London Dry Gin"). Information for bottle size (750ml) and alcohol % (40%) are also to be included. Governmental safety warnings are not required. We are open to use of any colours in the label. The basic label design would be re-used for different types of batches where we would change the style and alcohol name.
Updates

Target Market(s)

Up scale premium spirits buyers

Font styles to use
Serif
Sans Serif

Requirements
Must have
• A visual reference to the docks or the lake per the images attached.
Nice to have
• Ideally we can re-use the label design for a different type of Alcohol by changing the alcohol name and style information and maybe the colour of a major element in the label.

```html
<!DOCTYPE html>
<html lang="en">
<head>
<meta charset="utf-8">
<title>Seven Herons Distillery – Tuberix Vodka Label</title>
<link rel="stylesheet" href="https://fonts.googleapis.com/css2?family=Oswald:wght@600&family=Open+Sans:ital,wght@0,400;0,600;0,700;1,400&family=Pinyon+Script&display=swap">
<style>
  :root {
    --page: #f3f3f4;
    --navy: #2b2f44;
    --navy-deep: #1f2336;
    --brand-text: #cfd2da;
    --label-light: #e4e5e8;
    --label-light-2: #d3d5da;
    --ink: #3a3e52;
    --rule: #6e7285;
    --band-text: #d9dbe2;
  }
  * { margin: 0; padding: 0; box-sizing: border-box; }
  html, body { width: 1200px; height: 1200px; overflow: hidden; background: var(--page); }
  .canvas { position: relative; width: 1200px; height: 1200px; }

  /* Transparent upper label: lake outline area with brand name */
  .brand-mark { position: absolute; left: 222px; top: 155px; width: 700px; height: 438px; }
  .lake-outline { position: absolute; inset: 0; }
  .brand-name {
    position: absolute; left: 0; right: 0; top: 196px;
    text-align: center;
    font-family: 'Open Sans', sans-serif; font-weight: 600;
    font-size: 40px; line-height: 1.2; letter-spacing: 0.02em;
    color: var(--brand-text); white-space: nowrap;
  }

  /* Lower product label */
  .product-label {
    position: absolute; left: 168px; top: 665px; width: 863px; height: 380px;
    background: linear-gradient(90deg, var(--label-light) 0%, var(--label-light-2) 55%, var(--label-light) 100%);
  }
  .product-label .top-rule { position: absolute; left: 0; right: 0; top: 8px; height: 3px; background: var(--navy); }
  .product-name {
    position: absolute; left: 24px; top: 38px;
    font-family: 'Oswald', sans-serif; font-weight: 600; font-size: 94px; line-height: 1;
    letter-spacing: 0.1em; color: var(--ink); text-transform: uppercase;
  }
  .v-divider { position: absolute; left: 486px; top: 34px; width: 2px; height: 125px; background: var(--rule); }
  .spirit-type { position: absolute; left: 500px; right: 0; top: 42px; text-align: center; color: var(--ink); }
  .spirit-type .style { font-family: 'Pinyon Script', cursive; font-size: 46px; line-height: 1.1; display: block; }
  .spirit-type .kind { font-family: 'Open Sans', sans-serif; font-weight: 700; font-size: 44px; line-height: 1.2; display: block; letter-spacing: 0.02em; }
  .h-rule { position: absolute; left: 22px; right: 14px; height: 2px; background: var(--rule); }
  .h-rule.upper { top: 185px; }
  .h-rule.lower { top: 258px; }
  .details {
    position: absolute; left: 24px; right: 24px; top: 196px; height: 56px;
    display: flex; align-items: center;
    font-family: 'Open Sans', sans-serif; font-size: 21px; letter-spacing: 0.08em;
    color: var(--ink); text-transform: uppercase;
  }
  .details .num { font-style: italic; font-size: 28px; letter-spacing: 0.04em; margin-left: 12px; text-transform: none; }
  .details .sep { width: 2px; height: 34px; background: var(--rule); margin: 0 14px; }
  .details .water { margin-left: auto; }
  .spec-band {
    position: absolute; left: 0; right: 0; top: 279px; height: 86px;
    background: linear-gradient(90deg, var(--navy) 0%, #555a6e 40%, var(--navy-deep) 100%);
    display: flex; align-items: center; justify-content: space-between; padding: 0 50px;
    font-family: 'Open Sans', sans-serif; font-size: 21px; letter-spacing: 0.09em;
    color: var(--band-text); text-transform: uppercase; white-space: nowrap;
  }
  .spec-band .stars { font-size: 15px; letter-spacing: 0.2em; margin: 0 8px; }
</style>
</head>
<body>
<main class="canvas">
  <section class="brand-mark">
    <svg class="lake-outline" viewBox="0 0 700 438" role="img" aria-label="Outline map of Lac Vernisse">
      <defs>
        <linearGradient id="lakeTone" x1="0" y1="0" x2="1" y2="0">
          <stop offset="0" stop-color="#8a8e9c"/>
          <stop offset="0.5" stop-color="#2b2f44"/>
          <stop offset="1" stop-color="#50556b"/>
        </linearGradient>
      </defs>
      <rect x="0" y="0" width="700" height="438" rx="24" fill="url(#lakeTone)"/>
    </svg>
    <p class="brand-name">Seven Herons Distillery</p>
  </section>

  <section class="product-label">
    <div class="top-rule"></div>
    <h1 class="product-name">Tuberix</h1>
    <div class="v-divider"></div>
    <p class="spirit-type"><span class="style">Russian Potato</span><span class="kind">VODKA</span></p>
    <div class="h-rule upper"></div>
    <div class="details">
      <span>Bottle N.</span><span class="num">01</span>
      <span class="sep"></span>
      <span>Batch</span><span class="num">2020</span>
      <span class="sep"></span>
      <span class="water">Lac Vernisse Water</span>
    </div>
    <div class="h-rule lower"></div>
    <div class="spec-band">
      <span>40% Alc.</span>
      <span><span class="stars">★★</span>Handcrafted · Small Batch<span class="stars">★★</span></span>
      <span>750ML</span>
    </div>
  </section>
</main>
</body>
</html>
```